Creative Businesss Card desgin!

Create a business card for our business Gleam window cleaning!
We are open to creative ideas as long as it maintains a professional image.

Target Market(s)

Small Commercial window cleaning clients including car dealerships, strata manager, cafe

Industry/Entity Type

Window Cleaning

Contact Information for Business Card

Daniel Prescott
General Manager
Gleam Window Cleaning

daniel@gleamservices.com.au
pane-care-southbank.com.au
Ph: 1800 GET GLEAM
Mob: 0437 582 061

Colors
fbed22
0392cd

Requirements
Should not have
• Stock window cleaning/ squeegee graphics

```html
<!DOCTYPE html>
<html lang="en">
<head>
<meta charset="utf-8">
<title>Gleam Window Cleaning – Business Card</title>
<link rel="stylesheet" href="https://fonts.googleapis.com/css2?family=Lato:wght@300;400;700;900&display=swap">
<style>
  :root {
    --brand-blue: #1c5f9a;
    --brand-yellow: #f3e52b;
    --card-white: #ffffff;
    --ink-soft: #4a6a86;
    --stage: #e8e6e2;
    --shadow: rgba(30, 40, 50, 0.18);
  }
  * { box-sizing: border-box; margin: 0; padding: 0; }
  html, body {
    width: 771px;
    height: 1200px;
    overflow: hidden;
    background: var(--stage);
    font-family: "Lato", sans-serif;
  }
  .sheet {
    width: 771px;
    height: 1200px;
    display: flex;
    flex-direction: column;
    align-items: center;
    justify-content: center;
    gap: 90px;
  }
  .card {
    position: relative;
    width: 600px;
    height: 367px;
    background: var(--card-white);
    box-shadow: 0 8px 24px var(--shadow);
    overflow: hidden;
  }

  /* Front side */
  .card-front__art {
    position: absolute;
    inset: 0;
    width: 100%;
    height: 100%;
  }
  .identity {
    position: absolute;
    left: 40px;
    top: 44px;
  }
  .identity__name {
    color: var(--card-white);
    font-weight: 400;
    font-size: 21px;
    letter-spacing: 0.5px;
    text-transform: uppercase;
  }
  .identity__role {
    color: var(--brand-yellow);
    font-weight: 300;
    font-size: 16px;
    margin-top: 4px;
  }
  .contact-list {
    position: absolute;
    left: 40px;
    bottom: 40px;
    list-style: none;
    display: flex;
    flex-direction: column;
    gap: 10px;
  }
  .contact-list__item {
    display: flex;
    align-items: center;
    gap: 12px;
    color: var(--card-white);
    font-size: 13.5px;
    font-weight: 300;
  }
  .contact-list__icon {
    width: 22px;
    height: 22px;
    flex: none;
  }
  .brand-tag {
    position: absolute;
    right: 34px;
    top: 34px;
    width: 116px;
    height: 64px;
    background: var(--brand-blue);
    display: flex;
    flex-direction: column;
    align-items: center;
    justify-content: center;
    color: var(--brand-yellow);
    font-weight: 900;
    text-transform: uppercase;
  }
  .brand-tag__name { font-size: 22px; letter-spacing: 1px; line-height: 1; }
  .brand-tag__sub { font-size: 7.5px; letter-spacing: 0.6px; margin-top: 4px; }

  /* Back side */
  .card-back {
    display: flex;
    flex-direction: column;
    align-items: center;
    padding-top: 46px;
  }
  .brand-block {
    width: 230px;
    height: 172px;
    background: var(--brand-blue);
    display: flex;
    flex-direction: column;
    align-items: center;
    justify-content: center;
    color: var(--brand-yellow);
    font-weight: 900;
    text-transform: uppercase;
  }
  .brand-block__name { font-size: 50px; letter-spacing: 3px; line-height: 1; }
  .brand-block__sub { font-size: 15px; letter-spacing: 1.2px; margin-top: 8px; }
  .service-list {
    list-style: none;
    display: flex;
    gap: 26px;
    margin-top: 26px;
  }
  .service-list__item {
    display: flex;
    align-items: center;
    gap: 5px;
    color: var(--ink-soft);
    font-size: 13px;
    font-weight: 400;
  }
  .service-list__tick { width: 12px; height: 12px; }
  .web-address {
    margin-top: 16px;
    color: var(--ink-soft);
    font-size: 13px;
    letter-spacing: 3px;
    font-weight: 400;
  }
</style>
</head>
<body>
<main class="sheet">

  <section class="card card-front" aria-label="Business card front">
    <svg class="card-front__art" viewBox="0 0 600 367" preserveAspectRatio="none" aria-hidden="true">
      <polygon points="0,0 250,0 390,367 0,367" fill="#1c5f9a"/>
      <polygon points="250,0 300,0 440,367 390,367" fill="#f3e52b"/>
    </svg>

    <div class="identity">
      <p class="identity__name">Daniel Prescott</p>
      <p class="identity__role">General Manager</p>
    </div>

    <ul class="contact-list">
      <li class="contact-list__item">
        <svg class="contact-list__icon" viewBox="0 0 22 22" aria-hidden="true">
          <circle cx="11" cy="11" r="11" fill="#f3e52b"/>
          <path d="M7 8.5c0-1 .8-1.8 1.8-1.8h4.4c1 0 1.8.8 1.8 1.8v5c0 1-.8 1.8-1.8 1.8H8.8c-1 0-1.8-.8-1.8-1.8z" fill="#1c5f9a"/>
          <circle cx="11" cy="11" r="1.8" fill="#f3e52b"/>
        </svg>
        <span>1800 GET GLEAM</span>
      </li>
      <li class="contact-list__item">
        <svg class="contact-list__icon" viewBox="0 0 22 22" aria-hidden="true">
          <circle cx="11" cy="11" r="11" fill="#f3e52b"/>
          <rect x="8" y="5.5" width="6" height="11" rx="1.2" fill="#1c5f9a"/>
          <rect x="9" y="7" width="4" height="6.5" fill="#f3e52b"/>
        </svg>
        <span>0437 582 061</span>
      </li>
      <li class="contact-list__item">
        <svg class="contact-list__icon" viewBox="0 0 22 22" aria-hidden="true">
          <circle cx="11" cy="11" r="11" fill="#f3e52b"/>
          <rect x="6" y="7.5" width="10" height="7" fill="#1c5f9a"/>
          <path d="M6 7.5l5 4 5-4" fill="none" stroke="#f3e52b" stroke-width="1"/>
        </svg>
        <span>daniel@gleamservices.com.au</span>
      </li>
      <li class="contact-list__item">
        <svg class="contact-list__icon" viewBox="0 0 22 22" aria-hidden="true">
          <circle cx="11" cy="11" r="11" fill="#f3e52b"/>
          <circle cx="11" cy="11" r="5.5" fill="none" stroke="#1c5f9a" stroke-width="1.3"/>
          <ellipse cx="11" cy="11" rx="2.4" ry="5.5" fill="none" stroke="#1c5f9a" stroke-width="1"/>
          <path d="M5.5 11h11" stroke="#1c5f9a" stroke-width="1"/>
        </svg>
        <span>pane-care-southbank.com.au</span>
      </li>
    </ul>

    <div class="brand-tag">
      <span class="brand-tag__name">Gleam</span>
      <span class="brand-tag__sub">Window Cleaning</span>
    </div>
  </section>

  <section class="card card-back" aria-label="Business card back">
    <div class="brand-block">
      <span class="brand-block__name">Gleam</span>
      <span class="brand-block__sub">Window Cleaning</span>
    </div>

    <ul class="service-list">
      <li class="service-list__item">
        <svg class="service-list__tick" viewBox="0 0 12 12" aria-hidden="true">
          <rect x="0.5" y="0.5" width="11" height="11" fill="none" stroke="#4a6a86"/>
          <path d="M2.5 6l2.5 2.5 5-6" fill="none" stroke="#1c5f9a" stroke-width="1.6"/>
        </svg>
        Window Cleaning
      </li>
      <li class="service-list__item">
        <svg class="service-list__tick" viewBox="0 0 12 12" aria-hidden="true">
          <rect x="0.5" y="0.5" width="11" height="11" fill="none" stroke="#4a6a86"/>
          <path d="M2.5 6l2.5 2.5 5-6" fill="none" stroke="#1c5f9a" stroke-width="1.6"/>
        </svg>
        Pressure Cleaning
      </li>
      <li class="service-list__item">
        <svg class="service-list__tick" viewBox="0 0 12 12" aria-hidden="true">
          <rect x="0.5" y="0.5" width="11" height="11" fill="none" stroke="#4a6a86"/>
          <path d="M2.5 6l2.5 2.5 5-6" fill="none" stroke="#1c5f9a" stroke-width="1.6"/>
        </svg>
        Gutter Cleaning
      </li>
    </ul>

    <p class="web-address">pane-care-southbank.com.au</p>
  </section>

</main>
</body>
</html>
```